Welding and farication business card

Business name Tbm Welding & Fabrication

I need a business card made for my welding and fabrication business that is bold and stands out. My business is both welding repairs on machinery and anything else you can imagine as well as fabricating new products. i have used this service before and was very happy with the out come of my design logo. i think the card should remain fairly simple and classy but also be bold. I think a black card would best be suited to the talk with my logo on it. i feel the back of the card should just have my logo and the front have my logo email, website and phone number and maybe incorporate a facebook and instagram simple if it can be made look good these arnt a necessity.
I have included both my logo and some business card ideas below

Target Market(s)

Farmers, heavy industry, earthmoving, trucking

Industry/Entity Type

Engineering

Contact Information for Business Card

0438517264
dale@tbmweldingandfabrication.com.au
www.tbmweldingandfabrication.com.au

Colors
33a6d7
0255a3

Requirements
Must have
• Dale Hutchins
my phone number 0438517264
my logo
Preferably a black card desgn
Nice to have
• List of what i do,
Sheds and carports
Ute trays
Stockyards
Trailers
Farm equipment
Stockcrates
Gateways and Entrances
Breakdowns
Maintenance
And lots more!

```html
<!DOCTYPE html>
<html lang="en">
<head>
<meta charset="utf-8">
<title>TBM Welding &amp; Fabrication – Business Card</title>
<link rel="stylesheet" href="https://fonts.googleapis.com/css2?family=Michroma&family=Open+Sans:wght@400;600;700&display=swap">
<style>
  :root {
    --stage: #2a2b2d;
    --brand-blue: #0a4a9a;
    --brand-sky: #33a6d7;
    --card-white: #ffffff;
    --ink: #3a3d44;
    --rule: #4a4d52;
  }
  * { margin: 0; padding: 0; box-sizing: border-box; }
  html, body { width: 1200px; height: 900px; overflow: hidden; }
  body { background: var(--stage); font-family: "Open Sans", sans-serif; position: relative; }

  .card {
    position: absolute;
    width: 640px;
    height: 366px;
    border-radius: 30px;
    overflow: hidden;
    box-shadow: 0 14px 30px rgba(0,0,0,.45);
  }

  /* Back of card */
  .card-back { left: 60px; top: 60px; background: var(--brand-blue); }
  .card-back .wordmark { color: var(--card-white); left: 50%; top: 50%; transform: translate(-50%, -50%); }

  .wordmark {
    position: absolute;
    font-family: "Open Sans", sans-serif;
    font-weight: 700;
    text-align: center;
    line-height: 1;
  }
  .wordmark .wordmark-initials { display: block; font-size: 64px; letter-spacing: 2px; }
  .wordmark .wordmark-trade { display: block; font-size: 15px; letter-spacing: 1px; margin-top: 6px; }

  /* Front of card */
  .card-front { left: 500px; top: 474px; background: var(--card-white); }
  .card-front .swoosh { position: absolute; inset: 0; }
  .card-front .wordmark { color: var(--brand-blue); right: 60px; top: 46px; }

  .divider { position: absolute; left: 40px; right: 40px; top: 196px; height: 1px; background: var(--rule); }

  .holder { position: absolute; left: 40px; top: 140px; }
  .holder-name { font-family: "Michroma", sans-serif; font-size: 20px; letter-spacing: 5px; color: var(--brand-blue); }
  .holder-title { font-size: 15px; color: var(--ink); margin-top: 2px; }

  .address { position: absolute; left: 370px; top: 214px; font-size: 13px; color: var(--ink); line-height: 1.35; }

  .contacts { position: absolute; left: 40px; top: 222px; list-style: none; }
  .contacts li { display: flex; align-items: center; gap: 10px; font-size: 15px; color: var(--ink); height: 26px; }
  .contacts svg { width: 16px; height: 16px; fill: var(--brand-blue); flex-shrink: 0; }
</style>
</head>
<body>

<section class="card card-back" aria-label="Card back">
  <div class="wordmark">
    <span class="wordmark-initials">TBM</span>
    <span class="wordmark-trade">WELDING &amp; FABRICATION</span>
  </div>
</section>

<section class="card card-front" aria-label="Card front">
  <svg class="swoosh" viewBox="0 0 640 366" preserveAspectRatio="none" aria-hidden="true">
    <path d="M250,0 L640,0 L640,70 Q540,4 250,0 Z" fill="#0a4a9a"/>
    <path d="M430,366 Q500,272 640,250 L640,366 Z" fill="#0a4a9a"/>
  </svg>

  <div class="wordmark">
    <span class="wordmark-initials">TBM</span>
    <span class="wordmark-trade">WELDING &amp; FABRICATION</span>
  </div>

  <div class="holder">
    <div class="holder-name">LEWIS CARTER</div>
    <div class="holder-title">CEO/Managing Director</div>
  </div>

  <div class="divider"></div>

  <div class="address">418 Alder Crest Avenue NW<br>Suite 210, Fernwood MI 49620</div>

  <ul class="contacts">
    <li>
      <svg viewBox="0 0 24 24" aria-hidden="true"><path d="M6.6 10.8a15 15 0 0 0 6.6 6.6l2.2-2.2c.3-.3.7-.4 1-.2 1.1.4 2.3.6 3.6.6.6 0 1 .4 1 1V20c0 .6-.4 1-1 1A17 17 0 0 1 3 4c0-.6.4-1 1-1h3.5c.6 0 1 .4 1 1 0 1.3.2 2.5.6 3.6.1.3 0 .7-.2 1z"/></svg>
      214-555-0176
    </li>
    <li>
      <svg viewBox="0 0 24 24" aria-hidden="true"><path d="M6 2h12v5H6zM4 8h16a2 2 0 0 1 2 2v7h-4v5H6v-5H2v-7a2 2 0 0 1 2-2zm4 8v4h8v-4z"/></svg>
      214-555-0176
    </li>
    <li>
      <svg viewBox="0 0 24 24" aria-hidden="true"><path d="M2 5h20v14H2zm2 2v.4l8 5.3 8-5.3V7zm0 2.8V17h16V9.8l-8 5.3z"/></svg>
      lcarter@mailbox-example.com
    </li>
    <li>
      <svg viewBox="0 0 24 24" aria-hidden="true"><path d="M12 2a10 10 0 1 0 0 20 10 10 0 0 0 0-20zm6.9 9h-3a15 15 0 0 0-1.4-6.3A8 8 0 0 1 18.9 11zM12 4.1c.9 1.2 1.8 3.6 1.9 6.9h-3.8c.1-3.3 1-5.7 1.9-6.9zM9.5 4.7A15 15 0 0 0 8.1 11h-3a8 8 0 0 1 4.4-6.3zM5.1 13h3a15 15 0 0 0 1.4 6.3A8 8 0 0 1 5.1 13zm6.9 6.9c-.9-1.2-1.8-3.6-1.9-6.9h3.8c-.1 3.3-1 5.7-1.9 6.9zm2.5-.6a15 15 0 0 0 1.4-6.3h3a8 8 0 0 1-4.4 6.3z"/></svg>
      www.harbourline-freight.com
    </li>
  </ul>
</section>

</body>
</html>
```